Email Banner for Technology Company

We need a new email banner. The purpose of the email banner is to make us look more professional as a business and keep all communications with clients uniform. The previous designs which we have included below have now become outdated as our brand has developed and we need the new banner to become more aligned and modern.

We are a marketing organization that specialises in lead generation, email newsletters are sent to prospects on a regular basis. Therefore, it is important that we have an aesthetically pleasing banner as this is the first real impression prospects have our business. First impressions matter.

We are looking for a new email banner design as the current design is now outdated and does not reflect who we are as a business.

The new banners are required for launch at the start of Q2.

There is future work in the pipeline for the winning design. We have multiple industry sites that will require the new design as well as creating each of these in multiple languages.

The design must include the Zentroval wording the tagline 'The Ultimate Research Library for Technology Pro's.
It needs to be creative and fun but still remain professional, sticking with the colour theme that already exists.

Requirements
Must have
• The design must include the Zentroval wording the tagline 'The Ultimate Research Library for Technology Pro's.

```html
<!DOCTYPE html>
<html lang="en">
<head>
<meta charset="UTF-8">
<title>Zentroval Email Banner</title>
<link rel="stylesheet" href="https://fonts.googleapis.com/css2?family=Montserrat:wght@400;500;700&display=swap">
<style>
  :root {
    --navy-deep: #020e3c;
    --navy: #041a55;
    --blue-mid: #0a4a9a;
    --blue-bright: #1596e6;
    --cyan-glow: #5fd6ff;
    --logo-blue: #5ab4e8;
    --text-white: #ffffff;
    --button-bg: #030b33;
    --button-text: #1e8fe0;
  }
  html, body {
    margin: 0;
    padding: 0;
    overflow: hidden;
    background: var(--navy-deep);
  }
  .banner {
    position: relative;
    width: 1200px;
    height: 225px;
    overflow: hidden;
    font-family: "Montserrat", sans-serif;
    background:
      radial-gradient(ellipse 520px 300px at 0% 60%, var(--blue-bright) 0%, var(--blue-mid) 35%, transparent 75%),
      radial-gradient(ellipse 420px 300px at 100% 30%, var(--blue-bright) 0%, var(--blue-mid) 40%, transparent 80%),
      linear-gradient(90deg, var(--blue-mid) 0%, var(--navy) 22%, var(--navy-deep) 45%, var(--navy) 70%, var(--blue-mid) 100%);
  }
  .glow-field {
    position: absolute;
    top: 0;
    height: 225px;
  }
  .glow-field--left {
    left: 0;
    width: 300px;
    background:
      radial-gradient(circle 70px at 40px 150px, rgba(95,214,255,0.75), transparent 100%),
      radial-gradient(circle 90px at 140px 60px, rgba(40,150,235,0.35), transparent 100%),
      radial-gradient(circle 80px at 120px 200px, rgba(60,170,245,0.4), transparent 100%);
  }
  .glow-field--right {
    right: 0;
    width: 220px;
    background:
      radial-gradient(circle 80px at 170px 40px, rgba(120,225,255,0.8), transparent 100%),
      radial-gradient(circle 60px at 200px 140px, rgba(60,180,245,0.45), transparent 100%),
      radial-gradient(circle 70px at 80px 100px, rgba(40,150,235,0.3), transparent 100%);
  }
  .brand {
    position: absolute;
    left: 246px;
    top: 92px;
    margin: 0;
    font-size: 34px;
    font-weight: 500;
    letter-spacing: -0.5px;
    line-height: 1;
    color: var(--logo-blue);
  }
  .tagline {
    position: absolute;
    left: 433px;
    top: 100px;
    margin: 0;
    font-size: 19px;
    font-weight: 400;
    letter-spacing: 1px;
    line-height: 1;
    color: var(--text-white);
    white-space: nowrap;
  }
  .tagline strong {
    font-weight: 700;
    letter-spacing: 0.2px;
  }
  .cta {
    position: absolute;
    left: 1045px;
    top: 161px;
    width: 120px;
    height: 33px;
    display: flex;
    align-items: center;
    justify-content: center;
    background: var(--button-bg);
    color: var(--button-text);
    font-size: 10px;
    font-weight: 700;
    letter-spacing: 0.2px;
    text-decoration: none;
  }
</style>
</head>
<body>
  <div class="banner">
    <div class="glow-field glow-field--left" role="img" aria-label="Decorative pattern of glowing rounded squares in bright cyan and blue"></div>
    <div class="glow-field glow-field--right" role="img" aria-label="Decorative pattern of glowing rounded squares in bright cyan and blue"></div>
    <p class="brand">Zentroval</p>
    <p class="tagline">The Ultimate <strong>Research Library</strong> for Technology Pros</p>
    <a class="cta" href="#">CLICK HERE</a>
  </div>
</body>
</html>
```